Natural deodorant label

Natural clean deodorant line. Need modernize label which can be sized for both the regular and travel size deodorants. 2.75 x 3" and 1x2". Important to highlight no baking soda and its natural. Also has no aluminum, preservatives, nor chemicals. Its gender inclusive and safe for all ages. Please see website at www.lorvatique.com. will attach current label. Will need a label that i would be able to update with new scents as they come. Want a clean look.
Updates

Need extra days to review

Target Market(s)

the working mother/wife that lives a clean healthy life and pushes that for her family

Industry/Entity Type

health and beauty/deodorant/natural

Colors

Designer to choose colors to be used in the design.

Requirements
Must have
• No baking soda and gender inclusive on label. Clean look. Very little to no picture art.
Nice to have
• Potentially a different color representing the different scents. A brief description of the deodorant scent underneath the scent name. This can be found under the drop down menu titled valdora deodorant scents on the website www.lorvatique.com. Area on front label for a small barcode.
Should not have
• misspelled words; dark label

```html
<!DOCTYPE html>
<html lang="en">
<head>
<meta charset="utf-8">
<title>Lorvatique – Valdora Deodorant Label</title>
<link href="https://fonts.googleapis.com/css2?family=Cinzel:wght@600&family=Italiana&family=IBM+Plex+Mono:wght@400&display=swap" rel="stylesheet">
<style>
  :root {
    --backdrop: #555555;
    --leaf-dark: #0f2a1c;
    --leaf-mid: #22513a;
    --leaf-light: #2f6a4a;
    --cream: #f6f0ea;
    --ink: #262626;
  }
  * { margin: 0; padding: 0; box-sizing: border-box; }
  html, body {
    width: 1200px; height: 1200px; overflow: hidden;
    background: var(--backdrop);
  }
  .label {
    position: absolute; left: 200px; top: 164px;
    width: 800px; height: 871px;
  }
  .label__foliage {
    position: absolute; inset: 0;
    background:
      radial-gradient(circle at 25% 20%, var(--leaf-light) 0%, transparent 45%),
      radial-gradient(circle at 80% 75%, var(--leaf-mid) 0%, transparent 50%),
      linear-gradient(160deg, var(--leaf-mid), var(--leaf-dark));
  }
  .label__panel {
    position: absolute; left: 67px; top: 81px;
    width: 665px; height: 708px;
    background: var(--cream);
    border: 2px solid var(--ink);
    color: var(--ink);
  }
  .brand {
    position: absolute; left: 0; right: 0; top: 60px;
    display: flex; flex-direction: column; align-items: center; gap: 22px;
  }
  .brand__dot {
    width: 70px; height: 70px; border-radius: 50%;
    background: var(--ink);
  }
  .brand__name {
    font-family: "Cinzel", serif; font-weight: 600;
    font-size: 38px; letter-spacing: 0.02em; line-height: 1;
  }
  .scent {
    position: absolute; left: 0; right: 0; top: 288px;
    text-align: center;
  }
  .scent__name {
    font-family: "Italiana", serif;
    font-size: 88px; line-height: 1; letter-spacing: 0.02em;
  }
  .scent__note {
    margin-top: 22px;
    font-family: "IBM Plex Mono", monospace;
    font-size: 19px; letter-spacing: 0.22em;
  }
  .claims {
    position: absolute; left: 81px; top: 488px;
    width: 505px; height: 120px;
    font-family: "IBM Plex Mono", monospace;
  }
  .claims__rule { position: absolute; background: var(--ink); }
  .claims__item {
    position: absolute; left: 1px;
    font-size: 19px; letter-spacing: 0.16em; line-height: 1;
  }
  .claims__text {
    position: absolute; left: 236px; top: 52px;
    font-size: 14.5px; line-height: 16px; letter-spacing: 0.02em;
  }
  .site {
    position: absolute; left: 0; right: 0; top: 652px;
    text-align: center;
    font-family: "IBM Plex Mono", monospace;
    font-size: 18px; letter-spacing: 0.06em;
  }
</style>
</head>
<body>
  <main class="label">
    <div class="label__foliage" role="img" aria-label="Photograph of dark green tropical monstera leaves"></div>
    <section class="label__panel">
      <header class="brand">
        <span class="brand__dot"></span>
        <span class="brand__name">Lorvatique</span>
      </header>

      <div class="scent">
        <h1 class="scent__name">VALDORA</h1>
        <p class="scent__note">TROPICAL PASSION</p>
      </div>

      <div class="claims">
        <span class="claims__rule" style="left:221px; top:0; width:2px; height:115px;"></span>
        <span class="claims__rule" style="left:0; top:38px; width:505px; height:2px;"></span>
        <span class="claims__rule" style="left:0; top:77px; width:223px; height:2px;"></span>
        <span class="claims__rule" style="left:0; top:117px; width:505px; height:2px;"></span>
        <span class="claims__item" style="top:11px;">100% NATURAL</span>
        <span class="claims__item" style="top:51px;">NO BAKING SODA</span>
        <span class="claims__item" style="top:89px;">NO ALUMINUM</span>
        <p class="claims__text">Made with all<br>natural ingredients, without<br>preservatives or chemicals</p>
      </div>

      <p class="site">www.lorvatique.com</p>
    </section>
  </main>
</body>
</html>
```